Business Card Design

We are looking for a double sided business card.

On one side would be our logo

On the Other Side

Martin Kolby
Sales and Marketing

Phone/Text Logo and 530-418-2763
Email Logo and info@plumvalepets.com
Website Logo and www.plumvalepets.com
Facebook Logo and plumvale pets
Instagram Logo and plumvale_pets

Target Market(s)

Pet owners

Contact Information for Business Card

In project description

Requirements
Must have
• Logo

```html
<!DOCTYPE html>
<html lang="en">
<head>
<meta charset="utf-8">
<title>Plumvale Pets – Business Card</title>
<link href="https://fonts.googleapis.com/css2?family=Montserrat:wght@400;600;700;800&display=swap" rel="stylesheet">
<style>
  :root{
    --bg:#3b3431;
    --card:#111111;
    --gold:#f6ab1c;
    --orange:#f7931e;
    --silver:#e4e4e4;
    --text:#f2f2f2;
  }
  *{box-sizing:border-box;margin:0;padding:0}
  html,body{width:1200px;height:786px;overflow:hidden}
  body{
    background:var(--bg);
    font-family:"Montserrat",sans-serif;
    display:flex;align-items:center;justify-content:center;gap:48px;
  }
  .card{
    width:540px;height:309px;background:var(--card);
    border-radius:4px;position:relative;
    box-shadow:0 10px 30px rgba(0,0,0,.45);
    display:flex;align-items:center;
  }
  .brand{display:flex;flex-direction:column;align-items:center;gap:10px}
  .brand-name{display:flex;align-items:center;gap:10px;
    font-weight:800;color:var(--silver);letter-spacing:1px;line-height:1}
  .brand-dot{border-radius:50%;background:var(--gold);flex:none}
  .brand-url{color:var(--gold);font-weight:600;letter-spacing:3px;text-transform:uppercase}

  /* contact side */
  .card--contact .brand{width:250px}
  .card--contact .brand-name{font-size:26px}
  .card--contact .brand-dot{width:18px;height:18px}
  .card--contact .brand-url{font-size:9px}
  .divider{width:1.5px;height:160px;background:var(--gold);margin:0 30px 0 10px}
  .contact{color:var(--text)}
  .contact-name{font-size:22px;font-weight:800;color:var(--gold);line-height:1.1}
  .contact-role{font-size:14px;margin-bottom:10px}
  .contact-list{list-style:none;font-size:14px;line-height:1.5}
  .contact-list li{display:flex;align-items:center;gap:7px}
  .contact-list .gap{margin-top:10px}
  .icon{width:12px;height:12px;flex:none;fill:var(--gold)}
  .social-dot{width:11px;height:11px;border-radius:50%;background:var(--gold);flex:none}

  /* logo side */
  .card--logo{justify-content:center}
  .card--logo .brand-name{font-size:34px}
  .card--logo .brand-dot{width:22px;height:22px}
  .card--logo .brand-url{font-size:11px}
</style>
</head>
<body>
  <section class="card card--contact">
    <div class="brand">
      <div class="brand-name"><span class="brand-dot"></span>PLUMVALE PETS</div>
      <div class="brand-url">www.plumvalepets.com</div>
    </div>
    <div class="divider"></div>
    <div class="contact">
      <h1 class="contact-name">Martin Kolby</h1>
      <p class="contact-role">Sales and Marketing</p>
      <ul class="contact-list">
        <li><svg class="icon" viewBox="0 0 24 24"><path d="M6.6 10.8a15.1 15.1 0 0 0 6.6 6.6l2.2-2.2a1 1 0 0 1 1-.25 11.4 11.4 0 0 0 3.6.57 1 1 0 0 1 1 1V20a1 1 0 0 1-1 1A17 17 0 0 1 3 4a1 1 0 0 1 1-1h3.5a1 1 0 0 1 1 1c0 1.25.2 2.45.57 3.6a1 1 0 0 1-.25 1z"/></svg>530-418-2763</li>
        <li><svg class="icon" viewBox="0 0 24 24"><path d="M2 5h20v14H2z M2 5l10 8 10-8" stroke="#111" stroke-width="1.5"/></svg>info@plumvalepets.com</li>
        <li><svg class="icon" viewBox="0 0 24 24"><circle cx="12" cy="12" r="10"/><path d="M2 12h20M12 2c3 3 3 17 0 20M12 2c-3 3-3 17 0 20" stroke="#111" stroke-width="1.5" fill="none"/></svg>www.plumvalepets.com</li>
        <li class="gap"><span class="social-dot"></span>plumvale pets</li>
        <li><span class="social-dot"></span>plumvale_pets</li>
      </ul>
    </div>
  </section>

  <section class="card card--logo">
    <div class="brand">
      <div class="brand-name"><span class="brand-dot"></span>PLUMVALE PETS</div>
      <div class="brand-url">www.plumvalepets.com</div>
    </div>
  </section>
</body>
</html>
```